International Hand & Body company needing a Hand cream tube design for the Retail market

I am wanting a modern design for a new range of 6 hand creams I will be launching in August. They need to compliment our range of wrapped soaps which you can see on www.plomvane.com.au so am wanting clean designs. I am wanting a solid colour with a hand drawn organic feel line drawing in black elegantly placed wrapping around the label. I am wanting to focus on the colour and positioning of words and fonts. I like modern clean contemporary fonts. The final design needs to appeal to the broader female market.This may lead to range expansion if designs are well received.
Updates

These designs are not hitting the brief. They are too generic and look like a supermarket brand. Our brand is more boutique and this design needs to be modern and simple. I would like more solid colours and more modern designs. Without patterns.

Target Market(s)

Female aged 20 - 70

Requirements
Must have
• a modern contemporary design that will appeal to the masses.
• Please read attached brief.
Should not have
• a black botanical illustration, in a loose and organic design to match the fragrance.

```html
<!DOCTYPE html>
<html lang="en">
<head>
<meta charset="utf-8">
<title>Hand Cream Tube Labels</title>
<link rel="stylesheet" href="https://fonts.googleapis.com/css2?family=Lato:wght@400&family=Montserrat:ital,wght@0,400;0,700;1,700&family=Oswald:wght@300;500;700&display=swap">
<style>
:root{
  --pink:#e2217f;
  --navy:#1e2733;
  --tan:#b0a180;
  --ink:#111111;
  --white:#ffffff;
  --fold:#f0a8a8;
  --cut:#e0303a;
  --cond:"Oswald",sans-serif;
  --body:"Montserrat",sans-serif;
  --brand:"Lato",sans-serif;
}
*{margin:0;padding:0;box-sizing:border-box}
html,body{width:1154px;height:1200px;overflow:hidden;background:var(--white)}
.canvas{position:relative;width:1154px;height:1200px}

.label{position:absolute;top:0;width:540px;height:700px;color:var(--ink);--fg:var(--ink)}
.label--white{left:0}
.label--navy{left:618px;color:var(--tan);--fg:var(--tan)}
.label__bg{position:absolute;left:29px;width:507px;top:35px;height:632px;background:var(--navy)}
.label__band{position:absolute;left:29px;width:507px;top:121px;height:13px;background:var(--tan)}
.bleed{position:absolute;left:29px;width:507px;background:var(--pink)}
.bleed--top{top:0;height:35px}
.bleed--bottom{top:670px;height:24px}
.cut-h{position:absolute;left:29px;width:507px;border-top:1px dashed var(--cut)}
.fold{position:absolute;top:0;height:694px;border-left:1px dashed var(--fold)}
.fold--cut{border-left-color:var(--cut);top:37px;height:630px}

.brand{position:absolute;top:78px;width:200px;text-align:center;font-family:var(--brand);font-size:30px;letter-spacing:5px;color:var(--fg);transform:translateX(-50%)}

.swatch{position:absolute;left:97px;top:121px;width:142px;height:189px;background:var(--tan)}

.scent{position:absolute;font-family:var(--cond);font-weight:700;line-height:1}
.scent--front{left:167px;top:388px;transform:translateX(-50%) scaleX(.82);font-size:40px;white-space:nowrap;letter-spacing:-.5px}
.scent--front .accent{color:var(--tan)}
.scent--vertical{left:164px;top:349px;transform:translate(-50%,-50%) rotate(-90deg) scaleX(.88);font-size:40px;letter-spacing:1px;white-space:nowrap;color:var(--tan)}

.claims{position:absolute;text-align:right;font-family:var(--body);font-style:italic;font-weight:700;font-size:8.6px;line-height:10.7px;color:var(--fg)}

.desc{position:absolute;left:167px;top:543px;transform:translateX(-50%);width:190px;text-align:right;font-family:var(--body);font-size:10px;line-height:14.5px;white-space:nowrap}
.label--navy .desc{text-align:center}
.rule{position:absolute;height:1px;background:var(--fg)}
.product{position:absolute;left:167px;top:580px;transform:translateX(-50%);font-family:var(--cond);font-weight:300;font-size:28px;line-height:31px;white-space:nowrap}
.origin{position:absolute;left:167px;top:626px;transform:translateX(-50%);font-family:var(--cond);font-weight:500;font-size:8.6px;white-space:nowrap}
.volume{position:absolute;left:167px;top:637px;transform:translateX(-50%);font-family:var(--body);font-size:11px;white-space:nowrap}

.info{position:absolute;right:55px;text-align:right;font-family:var(--cond);font-weight:500;text-transform:uppercase;white-space:nowrap;color:var(--fg);transform-origin:right top}
.ingredients{top:202px;font-size:8px;line-height:10.8px;font-weight:300;transform:scaleX(.78)}
.ingredients b{font-weight:700}
.warnings{top:337px;font-size:8.6px;line-height:10.8px;transform:scaleX(.8)}
.usage{top:382px;font-size:8.6px;line-height:10.8px;transform:scaleX(.8)}

.suit{position:absolute;left:310px;width:175px;top:531px;text-align:center;font-family:var(--body);font-weight:700;font-size:8.6px;color:var(--fg)}
.icons{position:absolute;left:310px;top:548px;width:175px;display:flex;justify-content:space-between;align-items:center}
.icon{width:21px;height:21px;background:var(--fg)}
.icon--social{border-radius:4px}
.icon--badge{border-radius:50%}
.code{position:absolute;left:488px;top:574px;transform:rotate(-90deg);transform-origin:left top;font-family:var(--body);font-size:5.5px;white-space:nowrap}
.address{position:absolute;left:310px;width:175px;top:585px;text-align:center;font-family:var(--body);font-weight:700;font-size:6.6px;white-space:nowrap;letter-spacing:-.1px}
.contact{position:absolute;left:310px;width:175px;top:601px;display:flex;justify-content:space-between;font-family:var(--body);font-weight:700;font-size:7.2px;white-space:nowrap;letter-spacing:-.1px}

.sleeve{position:absolute;overflow:hidden}
.sleeve--white{left:1px;top:785px;width:429px;height:414px;border:1px solid var(--ink);background:var(--white)}
.sleeve--navy{left:702px;top:752px;width:429px;height:414px;background:var(--navy)}
.sleeve__fold{position:absolute;left:0;width:100%;border-top:1px dashed var(--ink)}
.sleeve--navy .sleeve__fold{border-top-color:#c8c0a8}
.sleeve__block{position:absolute;left:-1px;top:159px;width:189px;height:108px;background:var(--tan)}
.sleeve__title{position:absolute;font-family:var(--cond);font-weight:700;line-height:1;white-space:nowrap;font-size:44px}
.sleeve--white .sleeve__title{left:113px;top:202px;color:var(--tan);transform:scaleX(.82);transform-origin:left top;letter-spacing:-.5px}
.sleeve--white .sleeve__title .lead{color:var(--white)}
.sleeve--navy .sleeve__title{left:50%;top:180px;transform:translateX(-50%);color:var(--tan);letter-spacing:1.5px;font-size:42px}
.sleeve__sig{position:absolute;font-family:var(--brand);font-size:23px;letter-spacing:1px}
.sleeve__sig span{letter-spacing:4px;margin-left:4px}
.sleeve--white .sleeve__sig{left:14px;top:372px;color:var(--ink)}
.sleeve--navy .sleeve__sig{left:14px;top:376px;color:var(--tan)}
</style>
</head>
<body>
<div class="canvas">

  <!-- White tube label -->
  <section class="label label--white">
    <div class="bleed bleed--top"></div>
    <div class="bleed bleed--bottom"></div>
    <div class="cut-h" style="top:37px"></div>
    <div class="cut-h" style="top:667px"></div>
    <div class="fold" style="left:167px"></div>
    <div class="fold fold--cut" style="left:283px"></div>
    <div class="fold" style="left:398px"></div>

    <div class="brand" style="left:167px">plomvane</div>
    <div class="swatch"></div>
    <div class="scent scent--front">YUZU &amp; <span class="accent">SAGE</span></div>

    <div class="claims" style="right:290px;top:492px">• No Sulfates<br>• No Parabens<br>• No Mineral Oils<br>• No Artifical Colours</div>
    <p class="desc">A nourishing non-greasy hand<br>cream to keep skin soft &amp; hydrated.</p>
    <div class="rule" style="left:84px;width:168px;top:577px"></div>
    <div class="product">HAND CREAM</div>
    <div class="rule" style="left:84px;width:168px;top:613px"></div>
    <div class="origin">MADE IN AUSTRALIA</div>
    <div class="volume">35mL ℮ 1.18 fl. oz.</div>

    <div class="brand" style="left:398px">plomvane</div>
    <div class="claims" style="right:55px;top:148px">• No Sulfates<br>• No Parabens<br>• No Mineral Oils<br>• No Artifical Colours</div>
    <div class="rule" style="left:398px;width:87px;top:195px"></div>
    <div class="info ingredients"><b>Ingredients:</b> Aqua, Helianthus Annuus<br>Seed (Sunflower)Oil, Stearic Acid,<br>Glycerin, Cetearyl Alcohol, Beeswax,<br>Glyceryl Stearate, Dimethicone, Prunus<br>Amygdalus Dulcis (Almond) Oil, Parfum,<br>Phenoxyethanol, Triethanolamine, Tocopheryl<br>Acetate, Caprylyl Glycol, Sodium PCA, Disodium EDTA,<br>Aloe Barbadensis Leaf Juice (Aloe Vera) Powder,<br>Decylene Glycol, Theobroma Cacao Seed (Cocoa)<br>Butter, Cocos Nucifera (Coconut) Oil,<br>Butyrospermum Parkii (Shea) Butter</div>
    <div class="rule" style="left:330px;width:155px;top:329px"></div>
    <div class="info warnings">Discontinue use if irritation occurs.<br>Keep away from children.<br>Avoid contact with eyes.</div>
    <div class="rule" style="left:398px;width:87px;top:375px"></div>
    <div class="info usage">Massage into clean<br>dry skin as needed.</div>
    <div class="rule" style="left:415px;width:70px;top:409px"></div>

    <div class="rule" style="left:310px;width:175px;top:528px"></div>
    <div class="suit">SUITABLE FOR ALL SKIN TYPES</div>
    <div class="rule" style="left:310px;width:175px;top:544px"></div>
    <div class="icons" aria-label="Social and certification marks">
      <span class="icon icon--social"></span><span class="icon icon--social"></span>
      <span class="icon icon--badge"></span><span class="icon icon--badge"></span>
      <span class="icon icon--badge"></span><span class="icon icon--badge"></span>
    </div>
    <div class="code">Code: 418937</div>
    <div class="rule" style="left:310px;width:175px;top:580px"></div>
    <div class="address">Unit 5 / 12 Larkfield Road Brightmoor VIC 3100</div>
    <div class="rule" style="left:310px;width:175px;top:597px"></div>
    <div class="contact"><span>plomvane.com.au</span><span>|</span><span>sales@plomvane.com.au</span></div>
    <div class="rule" style="left:310px;width:175px;top:613px"></div>
  </section>

  <!-- Navy tube label -->
  <section class="label label--navy">
    <div class="label__bg"></div>
    <div class="label__band"></div>
    <div class="bleed bleed--top"></div>
    <div class="bleed bleed--bottom"></div>
    <div class="cut-h" style="top:37px"></div>
    <div class="cut-h" style="top:667px"></div>
    <div class="fold" style="left:167px;border-left-color:#3a4250"></div>
    <div class="fold fold--cut" style="left:283px"></div>
    <div class="fold" style="left:397px;border-left-color:#3a4250"></div>

    <div class="brand" style="left:167px">plomvane</div>
    <div class="scent scent--vertical">CITRUS &amp; SEAGRASS</div>

    <p class="desc">A nourishing non-greasy hand<br>cream to keep skin soft &amp; hydrated.</p>
    <div class="rule" style="left:84px;width:168px;top:577px"></div>
    <div class="product">HAND CREAM</div>
    <div class="rule" style="left:84px;width:168px;top:613px"></div>
    <div class="origin">MADE IN AUSTRALIA</div>
    <div class="volume">35mL ℮ 1.18 fl. oz.</div>

    <div class="brand" style="left:397px">plomvane</div>
    <div class="claims" style="right:55px;top:148px">• No Sulfates<br>• No Parabens<br>• No Mineral Oils<br>• No Artifical Colours</div>
    <div class="rule" style="left:398px;width:87px;top:195px"></div>
    <div class="info ingredients"><b>Ingredients:</b> Aqua, Helianthus Annuus<br>Seed (Sunflower)Oil, Stearic Acid,<br>Glycerin, Cetearyl Alcohol, Beeswax,<br>Glyceryl Stearate, Dimethicone, Prunus<br>Amygdalus Dulcis (Almond) Oil, Parfum,<br>Phenoxyethanol, Triethanolamine, Tocopheryl<br>Acetate, Caprylyl Glycol, Sodium PCA, Disodium EDTA,<br>Aloe Barbadensis Leaf Juice (Aloe Vera) Powder,<br>Decylene Glycol, Theobroma Cacao Seed (Cocoa)<br>Butter, Cocos Nucifera (Coconut) Oil,<br>Butyrospermum Parkii (Shea) Butter</div>
    <div class="rule" style="left:330px;width:155px;top:329px"></div>
    <div class="info warnings">Discontinue use if irritation occurs.<br>Keep away from children.<br>Avoid contact with eyes.</div>
    <div class="rule" style="left:398px;width:87px;top:375px"></div>
    <div class="info usage">Massage into clean<br>dry skin as needed.</div>
    <div class="rule" style="left:415px;width:70px;top:409px"></div>

    <div class="rule" style="left:310px;width:175px;top:528px"></div>
    <div class="suit">SUITABLE FOR ALL SKIN TYPES</div>
    <div class="rule" style="left:310px;width:175px;top:544px"></div>
    <div class="icons" aria-label="Social and certification marks">
      <span class="icon icon--social"></span><span class="icon icon--social"></span>
      <span class="icon icon--badge"></span><span class="icon icon--badge"></span>
      <span class="icon icon--badge"></span><span class="icon icon--badge"></span>
    </div>
    <div class="code">Code: 418937</div>
    <div class="rule" style="left:310px;width:175px;top:580px"></div>
    <div class="address">Unit 5 / 12 Larkfield Road Brightmoor VIC 3100</div>
    <div class="rule" style="left:310px;width:175px;top:597px"></div>
    <div class="contact"><span>plomvane.com.au</span><span>|</span><span>sales@plomvane.com.au</span></div>
    <div class="rule" style="left:310px;width:175px;top:613px"></div>
  </section>

  <!-- White sleeve -->
  <section class="sleeve sleeve--white">
    <div class="sleeve__fold" style="top:98px"></div>
    <div class="sleeve__fold" style="top:307px"></div>
    <div class="sleeve__block"></div>
    <div class="sleeve__title"><span class="lead">YUZU</span> &amp; SAGE</div>
    <div class="sleeve__sig">by<span>plomvane</span></div>
  </section>

  <!-- Navy sleeve -->
  <section class="sleeve sleeve--navy">
    <div class="sleeve__fold" style="top:99px"></div>
    <div class="sleeve__fold" style="top:308px"></div>
    <div class="sleeve__title">CITRUS &amp; SEAGRASS</div>
    <div class="sleeve__sig">by<span>plomvane</span></div>
  </section>

</div>
</body>
</html>
```